New Wine Brand bottle label-LumaBrio

We need a label designed for a new wine. The label should catch the customers eye with colors. It will be a red wine. We need a design that makes the customer think the wine has nutritional value and is unique when compared to other wines in that regard. Think: energized, vitality, healthy. Name of wine is LumaBrio

Target Market(s)

PPL aged 21-50 looking for healthy alternatives/supplements

Colors

Designer to choose colors to be used in the design.

Requirements
Must have
• eye catching label

```html
<!DOCTYPE html>
<html lang="en">
<head>
<meta charset="utf-8">
<title>LumaBrio – Wine Label</title>
<link rel="stylesheet" href="https://fonts.googleapis.com/css2?family=Questrial&display=swap">
<style>
  :root {
    --page-bg: #9a9a9a;
    --strip-bg: #f3d9dc;
    --art-magenta: #e0206e;
    --art-pink: #f25a93;
    --art-orange: #f39a2c;
    --art-purple: #8a3a9c;
    --art-lime: #b5c93a;
    --ink: #111111;
    --paper: #ffffff;
    --band: #0c0c0c;
    --band-text: #e9e9e9;
  }
  * { margin: 0; padding: 0; box-sizing: border-box; }
  html, body {
    width: 1200px;
    height: 1023px;
    overflow: hidden;
  }
  body {
    background: var(--page-bg);
    font-family: "Questrial", "Helvetica Neue", Arial, sans-serif;
    position: relative;
  }
  .label {
    position: absolute;
    left: 360px;
    top: 61px;
    width: 480px;
    height: 900px;
    overflow: hidden;
    background: var(--strip-bg);
  }
  .label__tagline {
    position: absolute;
    top: 0;
    left: 0;
    width: 100%;
    height: 56px;
    display: flex;
    align-items: center;
    justify-content: center;
    font-size: 18px;
    letter-spacing: 0.45em;
    padding-left: 0.45em;
    color: var(--ink);
    background: var(--strip-bg);
    white-space: nowrap;
  }
  .label__art {
    position: absolute;
    top: 56px;
    left: 0;
    width: 100%;
    height: 772px;
    background:
      radial-gradient(circle at 80% 12%, var(--art-orange) 0 22%, transparent 40%),
      radial-gradient(circle at 15% 10%, #f7c36a 0 12%, transparent 30%),
      radial-gradient(circle at 75% 80%, var(--art-lime) 0 8%, transparent 25%),
      radial-gradient(circle at 35% 85%, var(--art-purple) 0 12%, transparent 32%),
      linear-gradient(160deg, var(--art-pink) 0%, var(--art-magenta) 55%, #c21a66 100%);
  }
  .label__brand {
    position: absolute;
    left: 40px;
    top: 243px;
    width: 400px;
    height: 305px;
    background: var(--paper);
    border: 5px solid var(--ink);
    display: flex;
    flex-direction: column;
    justify-content: center;
    align-items: center;
    line-height: 1;
  }
  .label__brand-line {
    font-size: 118px;
    color: var(--ink);
    letter-spacing: 0.02em;
    white-space: nowrap;
  }
  .label__brand-line + .label__brand-line {
    margin-top: 14px;
  }
  .label__band {
    position: absolute;
    left: 0;
    bottom: 0;
    width: 100%;
    height: 72px;
    background: var(--band);
    color: var(--band-text);
    display: flex;
    justify-content: space-between;
    align-items: center;
    padding: 0 18px;
    font-size: 17px;
  }
</style>
</head>
<body>
  <section class="label">
    <div class="label__tagline">RADIANT RED</div>
    <div class="label__art" role="img" aria-label="Colourful abstract illustration of swirling magenta, pink, orange, purple and lime shapes and droplets"></div>
    <div class="label__brand">
      <span class="label__brand-line">LUMA</span>
      <span class="label__brand-line">BRIO</span>
    </div>
    <div class="label__band">
      <span class="label__volume">750ml</span>
      <span class="label__abv">13.5%Vol</span>
    </div>
  </section>
</body>
</html>
```